Looking for a label design for a product call KAVA. My business is to sell prepack kava to stores and online.
I need Hawaiian Polynesian theme around tradition.

The label need to have "Nalu Kava" that's the name of the product. Can add "traditional herbal drink"

Can be colorful, the label will be print in a oval shape clear label size 4.25"x3.25" and will be put on a black back ground.

I don't want any white.

Target Market(s)

Polynesian population and tourist

Industry/Entity Type

Business

Requirements
Must have
• Name: Nalu Kava
inscription: Traditional Herbal drink
inscription: 100% Dried Powder Kava Roots
Net Wt: 8oz
Nice to have
• Traditional art design.

```html
<!DOCTYPE html>
<html lang="en">
<head>
<meta charset="utf-8">
<title>Nalu Kava – Label</title>
<link rel="stylesheet" href="https://fonts.googleapis.com/css2?family=Roboto+Condensed:wght@700&family=Roboto:wght@700&display=swap">
<style>
  :root {
    --page: #ffffff;
    --page-frame: #d4d4d4;
    --rim-outer: #676237;
    --rim-inner: #6d3432;
    --ink-cream: #f4ec8e;
    --ink-name: #5a1a45;
    --leaf-light: #98f000;
    --leaf-dark: #5f9a18;
  }
  html, body {
    margin: 0;
    padding: 0;
    width: 1200px;
    height: 943px;
    overflow: hidden;
    background: var(--page);
  }
  .canvas {
    position: relative;
    width: 1200px;
    height: 943px;
  }
  .label { display: block; }
  .label__info {
    font-family: "Roboto Condensed", "Arial Narrow", sans-serif;
    font-weight: 700;
    fill: var(--ink-cream);
  }
  .label__tagline {
    font-family: "Roboto", Arial, sans-serif;
    font-weight: 700;
    fill: var(--ink-cream);
    letter-spacing: 2.6px;
  }
  .label__name {
    font-family: "Roboto Condensed", "Arial Narrow", sans-serif;
    font-weight: 700;
    fill: var(--ink-name);
    letter-spacing: 4px;
  }
</style>
</head>
<body>
<div class="canvas">
  <svg class="label" width="1200" height="943" viewBox="0 0 1200 943" xmlns="http://www.w3.org/2000/svg">
    <defs>
      <linearGradient id="label-base" x1="0" y1="0" x2="0" y2="1">
        <stop offset="0" stop-color="#d7653c"/>
        <stop offset="0.18" stop-color="#d9453f"/>
        <stop offset="0.34" stop-color="#b8654e"/>
        <stop offset="0.48" stop-color="#1fa15a"/>
        <stop offset="0.64" stop-color="#8f8a45"/>
        <stop offset="0.85" stop-color="#9a6a35"/>
        <stop offset="1" stop-color="#8c5a2e"/>
      </linearGradient>
      <radialGradient id="label-glow" cx="0.5" cy="0.48" r="0.5">
        <stop offset="0" stop-color="#f08b3e" stop-opacity="0.95"/>
        <stop offset="0.55" stop-color="#e07a42" stop-opacity="0.7"/>
        <stop offset="1" stop-color="#e07a42" stop-opacity="0"/>
      </radialGradient>
      <linearGradient id="label-edge" x1="0" y1="0" x2="0" y2="1">
        <stop offset="0" stop-color="#c9463c"/>
        <stop offset="0.5" stop-color="#2fb85a"/>
        <stop offset="0.85" stop-color="#9fb43a"/>
        <stop offset="1" stop-color="#f4ec1c"/>
      </linearGradient>
      <radialGradient id="leaf-fill" cx="0.5" cy="0.5" r="0.6">
        <stop offset="0" stop-color="var(--leaf-light)"/>
        <stop offset="1" stop-color="var(--leaf-dark)"/>
      </radialGradient>
    </defs>

    <rect class="page-frame" x="4.5" y="4.5" width="1191" height="934" rx="6" fill="none" stroke="var(--page-frame)" stroke-width="2"/>

    <g class="label__oval">
      <ellipse cx="600" cy="472" rx="387" ry="292" fill="var(--rim-outer)"/>
      <ellipse cx="600" cy="471" rx="366" ry="275" fill="var(--rim-inner)"/>
      <ellipse cx="600" cy="471" rx="360" ry="269" fill="url(#label-edge)"/>
      <ellipse cx="600" cy="466" rx="354" ry="262" fill="url(#label-base)"/>
      <ellipse cx="600" cy="466" rx="354" ry="262" fill="url(#label-glow)"/>
    </g>

    <text class="label__info" x="600" y="264" text-anchor="middle" font-size="24" textLength="304" lengthAdjust="spacingAndGlyphs">100% Dried Powder Kava Roots</text>
    <text class="label__info" x="599" y="297" text-anchor="middle" font-size="29" textLength="138" lengthAdjust="spacingAndGlyphs">Net Wt: 8oz</text>

    <text class="label__tagline" x="602" y="392" text-anchor="middle" font-size="22" textLength="375" lengthAdjust="spacingAndGlyphs">TRADITIONAL HERBAL DRINK</text>

    <text class="label__name" x="602" y="518" text-anchor="middle" font-size="148" textLength="625" lengthAdjust="spacingAndGlyphs">NALU KAVA</text>

    <rect class="label__leaves" role="img" aria-label="Illustration of bright green kava plant leaves"
          x="358" y="532" width="482" height="156" rx="78" fill="url(#leaf-fill)"/>
  </svg>
</div>
</body>
</html>
```